Real Estate Investor needs awesome business card design

I invest in real estate, focused on multi-family properties, and I need a business card to hand out to potential partners. I prefer simple, clean designs, but it needs to stand out, so I'd like there to be a bit of red in the design as well.

It should include this information:

Front
Dallin Pecksworth
Real Estate Investor
Direct phone: 502-867-3394
Email: dallinhpecksworth@quillmail.example
Headshot (Picture), I've uploaded a few, just pick the one you think looks best with your design. You can remove the background from the headshot image if it looks better.

Back
The back of the card's design should flow and be congruent with the front. On the back I want to put an inspirational quote or question. There will be different ones depending on the card, so I'll need the original file so I can edit it in the end.

For now, use “The Pessimist Sees Difficulty In Every Opportunity. The Optimist Sees The Opportunity In Every Difficulty.” -Barnaby Ellsworth

Target Market(s)

Investors

Industry/Entity Type

Real Estate

Contact Information for Business Card

Front
Dallin Pecksworth
Real Estate Investor

Back
The back of the card's design should flow and be congruent with the front. On the back I want to put an inspirational quote or question. There will be different ones depending on the card, so I'll need the original file so I can edit it in the end. I've uploaded some EXAMPLES of business cards with quotes on them. Don't copy but feel free to use them as inspiration.

The design will be printed on "ZIB sized" business cards
1039 x 697 pixels
with rounded corners

Font styles to use
Serif
Decorative
Script

Colors
ec1f27

Requirements
Must have
• Headshot, name, and other information in it.
• 1039 x 697 pixels
• Rounded corners
• Clean design that pops. I'm open to see any color background, including black.
• Headshots can be located here: https://www.filecrate.example/sh/8kd2wq7mzt31hvx/BBQTXP4ruf9LmQ0KhcvWx7b?dl=0
Nice to have
• It would be awesome if the design included a personal signature or monogram, but if not I'll get a personal logo developed later and the card redesigned if I think it needs it.
Should not have
• Cluttered design

```html
<!DOCTYPE html>
<html lang="en">
<head>
<meta charset="utf-8">
<title>Dallin Pecksworth — Business Card</title>
<link href="https://fonts.googleapis.com/css2?family=Open+Sans:wght@300;400;600;800&family=Handlee&display=swap" rel="stylesheet">
<style>
  :root {
    --stage-bg: #ececec;
    --card-dark: #2b2b2b;
    --card-mid: #333333;
    --band: rgba(40, 40, 40, 0.78);
    --band-line: #1e1e1e;
    --text-light: #d6d6d6;
    --text-soft: #bdbdbd;
    --accent: #ec1f27;
    --quote-mark: #8e2428;
  }
  html, body {
    margin: 0;
    padding: 0;
    width: 1200px;
    height: 801px;
    overflow: hidden;
    background: var(--stage-bg);
    font-family: "Open Sans", Arial, sans-serif;
  }
  .canvas {
    position: relative;
    width: 1200px;
    height: 801px;
    background: radial-gradient(ellipse at 50% 30%, #fafafa 0%, #e6e6e6 100%);
  }

  /* Front card */
  .card-front {
    position: absolute;
    left: 35px;
    top: 52px;
    width: 419px;
    height: 698px;
    border-radius: 26px;
    overflow: hidden;
    background: var(--card-dark);
  }
  .headshot {
    position: absolute;
    inset: 0;
    background:
      radial-gradient(ellipse 45% 35% at 50% 38%, #5a5a5a 0%, #3a3a3a 55%, transparent 100%),
      linear-gradient(180deg, #262626 0%, #2e2e2e 60%, #262626 100%);
  }
  .name-band {
    position: absolute;
    left: 0;
    top: 518px;
    width: 100%;
    height: 74px;
    background: var(--band);
    text-align: center;
  }
  .name {
    margin: 26px 0 0;
    font-size: 18px;
    font-weight: 400;
    letter-spacing: 4px;
    color: var(--text-light);
    line-height: 1;
  }
  .name .surname { color: var(--accent); font-weight: 600; }
  .role {
    margin: 6px 0 0;
    font-size: 12.5px;
    font-weight: 300;
    color: var(--text-soft);
  }
  .divider {
    position: absolute;
    left: 0;
    top: 592px;
    width: 100%;
    height: 6px;
    background: var(--band-line);
  }
  .contact-band {
    position: absolute;
    left: 0;
    top: 598px;
    width: 100%;
    height: 73px;
    background: var(--band);
    display: flex;
    justify-content: center;
    align-items: center;
    gap: 22px;
    font-size: 12px;
    font-weight: 300;
    color: var(--text-soft);
  }
  .contact-item { display: flex; align-items: center; gap: 6px; }
  .contact-item svg { width: 11px; height: 11px; fill: var(--text-soft); }

  /* Back card */
  .card-back {
    position: absolute;
    left: 467px;
    top: 194px;
    width: 698px;
    height: 419px;
    border-radius: 26px;
    overflow: hidden;
    background: radial-gradient(ellipse at 50% 30%, var(--card-mid) 0%, var(--card-dark) 70%);
  }
  .quote-mark {
    position: absolute;
    font-family: "Open Sans", Arial, sans-serif;
    font-weight: 800;
    font-size: 120px;
    line-height: 1;
    color: var(--quote-mark);
  }
  .quote-mark.open { left: 66px; top: 150px; }
  .quote-mark.close { left: 564px; top: 194px; }
  .quote-text {
    position: absolute;
    margin: 0;
    font-family: "Handlee", cursive;
    font-size: 14px;
    color: var(--text-light);
    line-height: 1;
    white-space: nowrap;
  }
  .quote-text.line-one { left: 117px; top: 180px; }
  .quote-text.line-two { left: 200px; top: 203px; }
  .attribution {
    position: absolute;
    right: 141px;
    top: 251px;
    margin: 0;
    font-size: 11px;
    letter-spacing: 3px;
    color: var(--text-soft);
    white-space: nowrap;
  }
</style>
</head>
<body>
<main class="canvas">
  <section class="card-front">
    <div class="headshot" role="img" aria-label="Black and white headshot of Dallin Pecksworth in a dark blazer"></div>
    <div class="name-band">
      <h1 class="name">DALLIN <span class="surname">PECKSWORTH</span></h1>
      <p class="role">Real Estate Investor</p>
    </div>
    <div class="divider"></div>
    <div class="contact-band">
      <span class="contact-item">
        <svg viewBox="0 0 24 24" aria-hidden="true"><path d="M6.6 10.8a15.1 15.1 0 0 0 6.6 6.6l2.2-2.2c.3-.3.7-.4 1-.2 1.1.4 2.3.6 3.6.6.6 0 1 .4 1 1V20c0 .6-.4 1-1 1C10.6 21 3 13.4 3 4c0-.6.4-1 1-1h3.5c.6 0 1 .4 1 1 0 1.3.2 2.5.6 3.6.1.3 0 .7-.2 1z"/></svg>
        502-867-3394
      </span>
      <span class="contact-item">
        <svg viewBox="0 0 24 24" aria-hidden="true"><path d="M2 5h20v2l-10 6L2 7z M2 9l10 6 10-6v10H2z"/></svg>
        dallinhpecksworth@quillmail.example
      </span>
    </div>
  </section>

  <section class="card-back">
    <span class="quote-mark open" aria-hidden="true">&ldquo;</span>
    <p class="quote-text line-one">The Pessimist Sees Difficulty In Every Opportunity.</p>
    <p class="quote-text line-two">The Optimist Sees The Opportunity In Every Difficulty.</p>
    <span class="quote-mark close" aria-hidden="true">&rdquo;</span>
    <p class="attribution">-&nbsp;&nbsp;BARNABY&nbsp;&nbsp;ELLSWORTH</p>
  </section>
</main>
</body>
</html>
```